Online radio: TunaWave homepage redesign

TunaWave is one of the world's leading brands of personalizable online radio -- similar to Melodex, but aimed at a somewhat older audience (age 35-54).

We'd like to redesign our homepage with a more contemporary look: It should emphasize our wide variety of GENRES (as the primary navigation), with the search field easy to find as a secondary navigation.

We'd like to retain our corporate color of maroon/plum. (We are not committed to the gold/yellow secondary color.)

See our current homepage at www.tunawave-example.com and our in-house attempt at an improved design at http://web4.tunawave-example.com/finder/2013ms/.

Ideally, we'd like to see designs for up to THREE different states:

(1) An initial state when users first come to the page.

(2) What the page would look like as the user is looking at channel options.

(3) What the page would look like once the media player is launched.

However, you may be able to combine (2) and (3) in a single screenshot.

Thanks!
Updates

At the request of several designers, we have decided to extend our deadline by four days. At the same time, we have increased our budget, including the addition of a 2nd place award. Thanks for your excellent work!

Thanks very much for your designs! We are very pleased with the overall quality of the work we are seeing. One reminder: As our brief says, the user interface "should emphasize our wide variety of GENRES (as the primary navigation), with the search field easy to find as a secondary navigation," and we feel that your design uses the SEARCH field as the primary navigation. Many of the designs use a large search field as the primary navigation. If yours does, you might want to tweak your design to put a greater emphasis on browsing genres as the primary navigation. Thanks and good luck!

Target Market(s)

Adults age 35-54 listening to online radio at work

Industry/Entity Type

Radio

Font styles to use
Sans Serif

Requirements
Must have
• This is a design/UI project -- we do not need code

```html
<!DOCTYPE html>
<html lang="en">
<head>
<meta charset="utf-8">
<title>TunaWave – Online Radio</title>
<link href="https://fonts.googleapis.com/css2?family=Open+Sans:wght@400;600;700&family=Roboto+Slab:wght@700&display=swap" rel="stylesheet">
<style>
:root{
  --plum:#5c0a46;
  --plum-tile:#6a1858;
  --gold:#f9c81e;
  --page:#efefef;
  --tile:#f0f0f0;
  --ink:#1d1d1d;
  --dark:#353535;
  --grey:#6b6b6b;
  --line:#cfcfcf;
}
*{margin:0;padding:0;box-sizing:border-box}
html,body{width:1200px;height:1085px;overflow:hidden}
body{background:var(--page);font-family:"Open Sans",sans-serif;color:var(--ink);position:relative}
.abs{position:absolute}
.site-header{position:absolute;left:0;top:0;width:1200px;height:78px;background:var(--plum)}
.brand{left:160px;top:20px;display:flex;align-items:center;gap:8px;color:#fff;font-weight:700;font-size:28px;letter-spacing:-1px}
.brand-dot{width:36px;height:36px;border-radius:50%;background:var(--gold)}
.nav-item{top:0;height:78px;line-height:76px;color:#fff;font-size:13.5px;letter-spacing:.5px}
.nav-item .dot{display:inline-block;width:7px;height:7px;border-radius:50%;background:#fff;margin-left:5px;vertical-align:1px}
.nav-genres{left:665px;width:97px;background:#fff;color:var(--plum);text-align:center}
.nav-genres .dot{background:var(--plum)}
.nav-signin{left:977px;width:63px;background:var(--gold);color:var(--plum);text-align:center}
.content{position:absolute;left:160px;top:78px;width:880px;height:1007px;background:#fff}
.headline{left:190px;top:130px;width:555px;text-align:center;font-size:32px;line-height:39px;font-weight:400}
.headline strong{color:var(--plum);font-weight:700}
.finder{left:190px;top:242px;width:555px;height:44px;background:var(--dark);color:#f3f3f3;font-size:16px;line-height:44px;padding-left:18px}
.finder svg,.side-search svg{position:absolute;right:16px;top:14px}
.tile{width:274px;height:161px;background:var(--tile);border:1px solid #e6e6e6}
.tile h3{text-align:center;font-size:16px;font-weight:700;margin-top:24px}
.tile .thumbs{position:absolute;top:56px;left:0;right:0;display:flex;justify-content:center;gap:5px}
.thumb{width:76px;height:76px}
.tile.active{background:var(--plum-tile);border-color:var(--plum-tile)}
.tile.active h3{color:var(--gold);margin-top:22px}
.tile.active .thumb{opacity:.35}
.play{left:113px;top:68px;width:42px;height:42px;border-radius:50%;background:#e9dfe6}
.side-search{left:768px;top:114px;width:242px;height:44px;background:var(--plum);color:#fff;font-size:17px;line-height:44px;padding-left:16px;letter-spacing:.5px}
.player{left:768px;top:168px;width:242px;height:426px;border:1px solid #d9d9d9;background:#fff;text-align:center}
.player h2{font-size:19px;line-height:24px;font-weight:700;margin-top:17px}
.album{position:absolute;left:59px;top:81px;width:125px;height:124px;background:linear-gradient(160deg,#b9ad93,#4a3c2e)}
.track{position:absolute;top:230px;width:100%;font-size:13px;line-height:16px}
.meta{position:absolute;top:274px;width:100%;font-size:9.5px;line-height:12px}
.progress{position:absolute;left:28px;top:322px;width:186px;height:1px;background:#d8d8d8}
.progress i{position:absolute;left:0;top:-1px;width:133px;height:2px;background:#444}
.time{position:absolute;top:330px;font-size:9.5px}
.controls{position:absolute;left:0;top:362px;width:242px;height:34px}
.ad{left:770px;top:614px;width:240px;height:200px;background:#2a0104;color:#fff;font-family:"Roboto Slab",serif;padding:14px 12px}
.ad p{font-size:17px;line-height:23px;font-weight:700}
.ad .gold{color:var(--gold);margin-top:2px}
.ad .buy{display:inline-block;background:#d3141b;font-family:"Open Sans",sans-serif;font-size:8px;font-weight:700;padding:2px 4px;margin-top:6px}
.ad .device{position:absolute;left:52px;top:116px;width:176px;height:70px;border-radius:8px;background:linear-gradient(90deg,#1a1a1a 0%,#444 50%,#e4e4e4 70%,#bdbdbd 100%)}
.ad .tag{position:absolute;left:12px;bottom:14px;font-family:"Open Sans",sans-serif;font-size:7.5px;font-weight:700;color:#f2d85a}
.ad .corner{position:absolute;right:0;top:0;width:14px;height:12px;background:#c9e2f2}
.rule{left:190px;top:898px;width:820px;height:2px;background:var(--line)}
.social{top:924px;width:22px;height:22px;border-radius:50%;background:#8a8a8a}
.divider{left:278px;top:915px;width:1px;height:43px;background:var(--plum)}
.footer-links{left:301px;top:922px;display:flex;gap:14px;font-size:12px;letter-spacing:.3px}
.copyright{left:301px;top:941px;font-size:9.5px;color:var(--grey)}
.apps-note{left:560px;top:922px;width:106px;text-align:right;font-size:11.5px;line-height:13px;color:var(--grey)}
.badge{top:924px;height:25px;border-radius:2px;background:#111}
.badge.violet{background:#6b1fa5}
.about-title{left:190px;top:973px;width:820px;height:16px}
.about-title::before{content:"";position:absolute;left:0;right:0;top:8px;height:2px;background:var(--line)}
.about-title span{position:absolute;left:22px;top:0;background:#fff;padding:0 6px;font-size:11.5px}
.about-text{left:188px;top:1006px;width:800px;font-size:11.3px;line-height:13.3px;color:var(--grey)}
.about-text a{color:var(--grey);margin-left:6px}
</style>
</head>
<body>
<header class="site-header">
  <div class="abs brand"><span class="brand-dot"></span>TunaWave</div>
  <div class="abs nav-item" style="left:579px">DJ PICKS<span class="dot"></span></div>
  <div class="abs nav-item nav-genres">GENRES<span class="dot"></span></div>
  <div class="abs nav-item" style="left:782px">SURPRISE ME</div>
  <div class="abs nav-item nav-signin">SIGNIN</div>
</header>

<main class="content"></main>

<h1 class="abs headline">Thousands of <strong>Radio Stations</strong> with Endless Music</h1>
<div class="abs finder">Find radio that plays your favorite
  <svg width="16" height="16" viewBox="0 0 16 16"><circle cx="6.5" cy="6.5" r="5" fill="none" stroke="#fff" stroke-width="2.4"/><line x1="10" y1="10" x2="15" y2="15" stroke="#fff" stroke-width="2.6" stroke-linecap="round"/></svg>
</div>

<section class="abs tile active" style="left:191px;top:317px">
  <h3>Top 40 / Pop Hits</h3>
  <div class="thumbs">
    <div class="thumb" role="img" aria-label="Pop singer portrait" style="background:#a0707f"></div>
    <div class="thumb" role="img" aria-label="Pop artist photo" style="background:#9a6a7e"></div>
    <div class="thumb" role="img" aria-label="Dancer silhouette artwork" style="background:#8a6a8a"></div>
  </div>
  <svg class="abs play" viewBox="0 0 42 42"><polygon points="17,13 30,21 17,29" fill="#6a1858"/></svg>
</section>
<section class="abs tile" style="left:473px;top:317px">
  <h3>Lite Hits</h3>
  <div class="thumbs">
    <div class="thumb" role="img" aria-label="Country singer portrait" style="background:linear-gradient(#6a6a6a,#2a2a2a)"></div>
    <div class="thumb" role="img" aria-label="Singer in sunglasses" style="background:linear-gradient(#c97d6b,#d9b07f)"></div>
    <div class="thumb" role="img" aria-label="Dancer silhouette artwork" style="background:linear-gradient(135deg,#1f3d5c,#9fc7e6)"></div>
  </div>
</section>
<section class="abs tile" style="left:191px;top:486px">
  <h3>Country</h3>
  <div class="thumbs">
    <div class="thumb" role="img" aria-label="Rock singer portrait" style="background:linear-gradient(#5a5a5a,#1e1e1e)"></div>
    <div class="thumb" role="img" aria-label="Jazz musician portrait" style="background:linear-gradient(#3a3a3a,#0c0c0c)"></div>
    <div class="thumb" role="img" aria-label="Dancer silhouette artwork" style="background:linear-gradient(135deg,#1f3d5c,#9fc7e6)"></div>
  </div>
</section>
<section class="abs tile" style="left:473px;top:486px">
  <h3>Classical</h3>
  <div class="thumbs">
    <div class="thumb" role="img" aria-label="Costumed performer" style="background:linear-gradient(#e8d9cf,#8c6a4f)"></div>
    <div class="thumb" role="img" aria-label="Conductor portrait" style="background:linear-gradient(#8a5a33,#1c1c1c)"></div>
    <div class="thumb" role="img" aria-label="Musician portrait" style="background:linear-gradient(#7a7a7a,#2e2e2e)"></div>
  </div>
</section>
<section class="abs tile" style="left:191px;top:655px">
  <h3>Classic Rock</h3>
  <div class="thumbs">
    <div class="thumb" role="img" aria-label="Musician portrait" style="background:linear-gradient(#7a7a7a,#2e2e2e)"></div>
    <div class="thumb" role="img" aria-label="Singer in sunglasses" style="background:linear-gradient(#c97d6b,#d9b07f)"></div>
    <div class="thumb" role="img" aria-label="Dancer silhouette artwork" style="background:linear-gradient(135deg,#1f3d5c,#9fc7e6)"></div>
  </div>
</section>
<section class="abs tile" style="left:473px;top:655px">
  <h3 style="margin-top:22px">Smooth Jazz</h3>
  <div class="thumbs" style="top:50px">
    <div class="thumb" role="img" aria-label="Jazz singer portrait" style="background:linear-gradient(#d0d0d0,#3a3a3a)"></div>
    <div class="thumb" role="img" aria-label="Singer portrait" style="background:linear-gradient(#8fb8d8,#e0c2a0)"></div>
    <div class="thumb" role="img" aria-label="Band group photo" style="background:linear-gradient(#5a4a3a,#b0503a)"></div>
  </div>
</section>

<div class="abs side-search">Search
  <svg width="16" height="16" viewBox="0 0 16 16"><circle cx="6.5" cy="6.5" r="5" fill="none" stroke="#fff" stroke-width="2.4"/><line x1="10" y1="10" x2="15" y2="15" stroke="#fff" stroke-width="2.6" stroke-linecap="round"/></svg>
</div>

<aside class="abs player">
  <h2>Long Summer Jams:<br>2K to Today</h2>
  <div class="album" role="img" aria-label="Album cover artwork"></div>
  <p class="track">Shake It Loose, Lyra Dawn feat.<br>Milo Hart Kobi Reyes</p>
  <p class="meta">2010<br>Harbor Records Vance / Lowe / Ortiz / Hale</p>
  <div class="progress"><i></i></div>
  <span class="time" style="left:26px">02:31</span>
  <span class="time" style="right:16px">00:31</span>
  <svg class="controls" viewBox="0 0 242 34">
    <circle cx="42" cy="17" r="16" fill="#eee" stroke="#ccc"/>
    <rect x="36" y="10" width="4.5" height="14" fill="#222"/><rect x="43.5" y="10" width="4.5" height="14" fill="#222"/>
    <circle cx="75" cy="17" r="12" fill="#eee" stroke="#ccc"/>
    <polygon points="70,12 77,17 70,22" fill="#222"/><rect x="77" y="12" width="2.5" height="10" fill="#222"/>
    <polygon points="96,15 99,15 103,11 103,23 99,19 96,19" fill="#333"/>
    <path d="M105 14 q2 3 0 6" fill="none" stroke="#333"/>
    <line x1="116" y1="17" x2="214" y2="17" stroke="#ccc"/>
    <circle cx="182" cy="17" r="5" fill="#5c0a46"/>
  </svg>
</aside>

<aside class="abs ad">
  <span class="corner"></span>
  <p>Go Prepaid Today<br>12GB @ ₹99</p>
  <p class="gold">Plug In. Tune In.</p>
  <span class="buy">Buy Now</span>
  <div class="device" role="img" aria-label="Wireless data card plugged into a laptop port"></div>
  <span class="tag">VOLTLINK</span>
</aside>

<div class="abs rule"></div>
<span class="abs social" style="left:190px"></span>
<span class="abs social" style="left:226px"></span>
<div class="abs divider"></div>
<nav class="abs footer-links"><span>HOME</span><span>NEWS</span><span>ABOUT</span><span>CONTACT</span></nav>
<p class="abs copyright">© Copyright 2014 tunawave-example.com</p>
<p class="abs apps-note">Get the free<br>TunaWave apps</p>
<span class="abs badge" style="left:681px;width:76px"></span>
<span class="abs badge" style="left:761px;width:77px"></span>
<span class="abs badge" style="left:842px;width:76px"></span>
<span class="abs badge violet" style="left:922px;width:88px"></span>

<div class="abs about-title"><span>ABOUT TUNAWAVE</span></div>
<p class="abs about-text">Lorem ipsum dolor sit amet, consectetur adipisicing elit, sed do eiusmod tempor incididunt ut labore et dolore magna aliqua. Ut enim ad minim veniam, quis nostrud exercitation ullamco laboris nisi ut aliquip ex ea commodo consequat. Duis aute irure dolor in reprehenderit in voluptate velit esse cillum dolore eu fugiat nulla pariatur. Excepteur sint occaecat cupidatat non proident, sunt <a href="#">Learn More</a></p>
</body>
</html>
```